Tech Savy small Business accountant business card design

We need a business card for a new company based in the cloud. We provide tax, business advisory, accounting, information technology solutions and back office functions to small businesses. We offer fixed fee packages with add on services as you need them. By harnessing technology we simplify small business operational processes providing valuable time and information for small business owners to grow their business. In the logo (quilbrook) we want to be able to see quil and experts. The final design should communicate achieving growth dreams and balance (ie life and $).
Updates
This project has been temporarily placed on hold until I finalize "Tech Savy small Business accountant needs a logo". I invite all designers to submit on this logo project. Once my logo is finalized I will resume this business card contest. Thanks Added Wednesday, March 19, 2014
This project has been temporarily placed on hold until I finalize "Tech Savy small Business accountant logo". I invite all designers to submit on this logo project. Once my logo is finalized I will resume this business card contest. Thanks Added Thursday, March 20, 2014
Target Market(s)
Small Business (Revenue $500,000, more than 3 employees) owners.
Industry/Entity Type
Small Business
Contact Information for Business Card
Marla Henwick (Principal)
Accountant, Tax Agent.
TEL | 0418 663 904
EMAIL | Marla.Henwick@quilbrook-mail.com.au
WEB | www.quilbrook-mail.com.au
Look and feel

```html
<!DOCTYPE html>
<html lang="en">
<head>
<meta charset="utf-8">
<title>quilbrook business card</title>
<link rel="stylesheet" href="https://fonts.googleapis.com/css2?family=Didact+Gothic&display=swap">
<style>
  :root {
    --page-bg: #d8d3cc;
    --card-light-top: #eef0f2;
    --card-light-bottom: #d4d8dd;
    --card-dark-top: #3a3537;
    --card-dark-bottom: #5b5456;
    --swoosh-blue: #1f78b8;
    --swoosh-blue-deep: #155f98;
    --swoosh-edge: #e9eef2;
    --brand-blue: #2a7fb0;
    --tagline-grey: #56585c;
    --text-light: #dcdad8;
    --text-soft: #cbc4bf;
    --icon-fill: #b9b2ad;
  }
  * { margin: 0; padding: 0; box-sizing: border-box; }
  html, body {
    width: 1200px;
    height: 970px;
    overflow: hidden;
    background: var(--page-bg);
    font-family: "Didact Gothic", "Century Gothic", sans-serif;
  }
  .card {
    position: absolute;
    left: 80px;
    top: 189px;
    width: 1040px;
    height: 592px;
    overflow: hidden;
    background: linear-gradient(180deg, var(--card-light-top), var(--card-light-bottom));
    box-shadow: 0 10px 30px rgba(0,0,0,0.18);
  }
  .card-waves {
    position: absolute;
    inset: 0;
    width: 1040px;
    height: 592px;
  }
  .brand-name {
    position: absolute;
    left: 50px;
    top: 52px;
    font-size: 132px;
    line-height: 1;
    letter-spacing: -3px;
    color: var(--brand-blue);
  }
  .tagline {
    position: absolute;
    left: 53px;
    top: 188px;
    font-size: 24px;
    color: var(--tagline-grey);
  }
  .person {
    position: absolute;
    left: 53px;
    top: 362px;
    color: var(--text-light);
  }
  .person-name {
    font-size: 44px;
    line-height: 1;
  }
  .person-role {
    font-size: 28px;
  }
  .person-title {
    font-size: 28px;
    line-height: 1.2;
    color: var(--text-soft);
  }
  .contact {
    position: absolute;
    left: 53px;
    top: 478px;
    list-style: none;
    font-size: 28px;
    color: var(--text-soft);
  }
  .contact-item {
    display: flex;
    align-items: center;
    gap: 12px;
    height: 36px;
  }
  .contact-icon { width: 28px; height: 24px; flex: none; }
  .website {
    position: absolute;
    right: 50px;
    top: 514px;
    height: 36px;
    line-height: 36px;
    font-size: 28px;
    color: var(--text-soft);
  }
</style>
</head>
<body>
  <section class="card">
    <svg class="card-waves" viewBox="0 0 1040 592" aria-hidden="true">
      <defs>
        <linearGradient id="swoosh" x1="0" y1="0" x2="1" y2="0">
          <stop offset="0" stop-color="var(--swoosh-blue-deep)"/>
          <stop offset="1" stop-color="var(--swoosh-blue)"/>
        </linearGradient>
        <linearGradient id="dark-panel" x1="0" y1="0" x2="0" y2="1">
          <stop offset="0" stop-color="var(--card-dark-top)"/>
          <stop offset="1" stop-color="var(--card-dark-bottom)"/>
        </linearGradient>
      </defs>
      <path class="swoosh-band" fill="url(#swoosh)"
        d="M0,330 C200,282 400,290 560,335 C760,380 960,330 1040,176 L1040,362 C920,372 760,375 600,345 C380,300 180,300 0,352 Z"/>
      <path class="dark-panel" fill="url(#dark-panel)"
        d="M0,352 C180,300 380,300 600,345 C760,375 920,372 1040,362 L1040,592 L0,592 Z"/>
      <path class="swoosh-edge" fill="none" stroke="var(--swoosh-edge)" stroke-width="2.5"
        d="M0,352 C180,300 380,300 600,345 C760,375 920,372 1040,362"/>
    </svg>

    <div class="brand-name">quilbrook</div>
    <p class="tagline">Your business, accounting and technology partner</p>

    <div class="person">
      <p class="person-name">Marla Henwick CPA <span class="person-role">(Principal)</span></p>
      <p class="person-title">Accounting, Tax and I.T. Solutions</p>
    </div>

    <ul class="contact">
      <li class="contact-item">
        <svg class="contact-icon" viewBox="0 0 28 24" aria-hidden="true">
          <rect x="0" y="0" width="28" height="24" fill="var(--icon-fill)"/>
          <path d="M5,9 C5,5 23,5 23,9 L20,11 L18,8 L10,8 L8,11 Z" fill="var(--card-dark-top)"/>
          <rect x="8" y="12" width="12" height="8" fill="var(--card-dark-top)"/>
        </svg>
        <span>0418 663 904</span>
      </li>
      <li class="contact-item">
        <svg class="contact-icon" viewBox="0 0 28 24" aria-hidden="true">
          <rect x="0" y="0" width="28" height="24" fill="var(--icon-fill)"/>
          <rect x="5" y="6" width="18" height="12" fill="none" stroke="var(--card-dark-top)" stroke-width="1.6"/>
          <path d="M5,6 L14,13 L23,6" fill="none" stroke="var(--card-dark-top)" stroke-width="1.6"/>
        </svg>
        <span>Marla.Henwick@quilbrook-mail.com.au</span>
      </li>
    </ul>

    <p class="website">www.quilbrook-mail.com.au</p>
  </section>
</body>
</html>
```